Tovimerra: Travel business card redesign

We need a clean elegant look for our cards featuring blue and orange. Look should communicate a sense of strong design and seem uncluttered. The company is Tovimerra which means Every trip, an escape. As in every trip is an Every trip, an escape. Feel free to reinvent the logo or just tweak it. Colors should be blue like Caribbean waters and a saturated orange. Keep it clean and simple.
Please match the information in the sample uploaded but the sample is horrible -- a non-starter -- use for information only. also please add managing director to my name as title

Target Market(s)
potential clients, hotels, trade publications
Industry/Entity Type
Travel Industry
Contact Information for Business Card
as above
Requirements
Must have
- Font should be century gothic. Colors below are close but a but prefer lighter in each case.

```html
<!DOCTYPE html>
<html lang="en">
<head>
<meta charset="utf-8">
<title>Tovimerra – Business Card</title>
<link rel="stylesheet" href="https://fonts.googleapis.com/css2?family=Jost:wght@400;600;700;800&display=swap">
<style>
  :root {
    --frame: #242424;
    --paper: #ffffff;
    --sea-blue: #5190cb;
    --band-orange: #d37033;
    --mark-orange: #d8873a;
    --ink-light: #ffffff;
  }
  * { box-sizing: border-box; margin: 0; padding: 0; }
  html, body {
    width: 1200px; height: 1200px; overflow: hidden;
    background: var(--paper);
    font-family: "Jost", "Century Gothic", sans-serif;
  }
  .canvas { position: relative; width: 1200px; height: 1200px; }

  .card {
    position: absolute;
    background: var(--frame);
  }
  .card--front { left: 163px; top: 65px; width: 849px; height: 488px; }
  .card--back  { left: 164px; top: 639px; width: 851px; height: 493px; }

  .panel { position: absolute; }
  .panel--white { background: var(--paper); }
  .panel--blue  { background: var(--sea-blue); color: var(--ink-light); }
  .panel--orange { background: var(--band-orange); color: var(--ink-light); }

  /* Front */
  .front-main { left: 23px; top: 20px; width: 804px; height: 285px; }
  .phone { top: 317px; height: 70px; width: 398px;
    display: flex; align-items: center; justify-content: center;
    font-size: 29px; font-weight: 400; letter-spacing: 0.5px; }
  .phone--office { left: 23px; }
  .phone--mobile { left: 429px; }
  .tollfree { left: 23px; top: 400px; width: 804px; height: 68px;
    display: flex; align-items: center; justify-content: center;
    font-size: 28px; font-weight: 700; }

  .brand {
    position: absolute;
    display: flex; flex-direction: column; align-items: flex-end;
  }
  .brand__name {
    color: var(--mark-orange);
    font-weight: 800;
    text-transform: uppercase;
    line-height: 1;
  }
  .brand__tagline {
    color: var(--sea-blue);
    font-weight: 600;
    line-height: 1;
  }
  .brand--small { left: 36px; top: 52px; }
  .brand--small .brand__name { font-size: 50px; letter-spacing: 6px; }
  .brand--small .brand__tagline { font-size: 24px; margin-top: 8px; }

  .address {
    position: absolute; left: 36px; top: 168px;
    color: var(--sea-blue); font-weight: 600; font-size: 21px; line-height: 28px;
  }
  .person {
    position: absolute; left: 476px; top: 54px;
    color: var(--sea-blue); font-weight: 600;
  }
  .person__name { font-size: 39px; line-height: 44px; }
  .person__title { font-size: 28px; line-height: 34px; }

  /* Back */
  .back-main { left: 22px; top: 26px; width: 804px; height: 361px; }
  .brand--large { left: 0; right: 0; top: 106px; align-items: center; }
  .brand--large .brand__stack { display: flex; flex-direction: column; align-items: flex-end; }
  .brand--large .brand__name { font-size: 92px; letter-spacing: 10px; }
  .brand--large .brand__tagline { font-size: 46px; margin-top: 12px; }

  .back-bar { left: 22px; top: 401px; width: 804px; height: 68px;
    display: flex; align-items: center; justify-content: space-between;
    padding: 0 58px 0 82px;
    font-size: 29px; font-weight: 600; }
</style>
</head>
<body>
<main class="canvas">

  <section class="card card--front" aria-label="Card front">
    <div class="panel panel--white front-main">
      <div class="brand brand--small">
        <span class="brand__name">Tovimerra</span>
        <span class="brand__tagline">Every trip, an escape</span>
      </div>
      <address class="address" style="font-style:normal">
        1460 Harbor Crest Way N.<br>
        Bayview, 90218
      </address>
      <div class="person">
        <p class="person__name">Dana Whitlow</p>
        <p class="person__title">Managing director</p>
      </div>
    </div>
    <div class="panel panel--blue phone phone--office">415.382.6604</div>
    <div class="panel panel--blue phone phone--mobile">628.514.2290</div>
    <div class="panel panel--orange tollfree">877.68.TOVIM (86846)</div>
  </section>

  <section class="card card--back" aria-label="Card back">
    <div class="panel panel--white back-main">
      <div class="brand brand--large">
        <div class="brand__stack">
          <span class="brand__name">Tovimerra</span>
          <span class="brand__tagline">Every trip, an escape</span>
        </div>
      </div>
    </div>
    <div class="panel panel--orange back-bar">
      <span class="back-bar__name">Dana Whitlow</span>
      <span class="back-bar__title">Managing director</span>
    </div>
  </section>

</main>
</body>
</html>
```